Business Card for Brevel Coatings

We need a simple, yet out standing business card for our painting company.

Target Market(s)

wealthy; high-end neighborhoods, and businesses

Industry/Entity Type

Painting

Contact Information for Business Card

Name:
Doran Vask

Email:
d.vask@brevel-coatings.com

Website:
Brevel-coatings.com

Phone Number:
(555) 416-9073

Font styles to use
Serif
Sans Serif

Requirements
Must have
• slogan "making change simple"
Should not have
• A title attached to the name on the card

```html
<!DOCTYPE html>
<html lang="en">
<head>
<meta charset="utf-8">
<title>Brevel Coatings – Business Card</title>
<link rel="stylesheet" href="https://fonts.googleapis.com/css2?family=Mulish:wght@400;700;800&display=swap">
<style>
  :root {
    --leaf: #b8cf3f;
    --forest: #3d5325;
    --paper: #ffffff;
    --card-edge: #e6e6e6;
    --card-shadow: #d2d2d2;
    --page: #ffffff;
  }
  * { margin: 0; padding: 0; box-sizing: border-box; }
  html, body {
    width: 1200px;
    height: 900px;
    overflow: hidden;
    background: var(--page);
    font-family: "Mulish", sans-serif;
  }
  .canvas {
    position: relative;
    width: 1200px;
    height: 900px;
  }
  .card {
    position: absolute;
    left: 296px;
    width: 593px;
    height: 363px;
    background: var(--paper);
    border: 1px solid var(--card-edge);
    box-shadow: 7px 7px 0 var(--card-shadow);
  }
  .card--front { top: 60px; }
  .card--back { top: 473px; }

  .side-label {
    position: absolute;
    left: 913px;
    font-size: 20px;
    font-weight: 400;
    color: var(--forest);
    letter-spacing: 0.2px;
  }
  .side-label--front { top: 406px; }
  .side-label--back { top: 822px; }

  .tile {
    position: absolute;
    width: 245px;
    height: 131px;
    padding: 13px 16px;
  }
  .tile--leaf { background: var(--leaf); color: var(--forest); }
  .tile--forest { background: var(--forest); color: var(--leaf); }

  .tile__label {
    display: block;
    font-size: 19px;
    font-weight: 400;
    line-height: 23px;
  }
  .tile__value {
    display: block;
    font-size: 19px;
    font-weight: 800;
    line-height: 24px;
  }

  /* front */
  .brand {
    position: absolute;
    left: 32px;
    top: 52px;
    display: flex;
    align-items: center;
    gap: 12px;
    color: var(--forest);
  }
  .brand__mark {
    width: 22px;
    height: 22px;
    background: var(--leaf);
  }
  .brand__name {
    font-size: 27px;
    font-weight: 800;
    letter-spacing: 0.3px;
    color: var(--forest);
  }
  .tile--front-top { left: 313px; top: 34px; }
  .tile--front-left { left: 34px; top: 199px; }
  .tile--slogan { left: 313px; top: 198px; padding-top: 12px; }

  /* back */
  .tile--name { left: 31px; top: 32px; padding: 13px 19px; }
  .tile--email { left: 311px; top: 32px; }
  .tile--website { left: 33px; top: 196px; }
  .tile--contact { left: 311px; top: 195px; }
</style>
</head>
<body>
<div class="canvas">

  <section class="card card--front" aria-label="Card front">
    <div class="brand">
      <span class="brand__mark"></span>
      <span class="brand__name">Brevel Coatings</span>
    </div>
    <div class="tile tile--leaf tile--front-top"></div>
    <div class="tile tile--leaf tile--front-left"></div>
    <div class="tile tile--forest tile--slogan">
      <span class="tile__label">making change</span>
      <span class="tile__value">simple</span>
    </div>
  </section>
  <span class="side-label side-label--front">front</span>

  <section class="card card--back" aria-label="Card back">
    <div class="tile tile--forest tile--name">
      <span class="tile__value">Doran Vask</span>
    </div>
    <div class="tile tile--leaf tile--email">
      <span class="tile__label">email</span>
      <span class="tile__value">d.vask@<br>brevel-coatings.com</span>
    </div>
    <div class="tile tile--leaf tile--website">
      <span class="tile__label">website</span>
      <span class="tile__value">Brevel-coatings.com</span>
    </div>
    <div class="tile tile--forest tile--contact">
      <span class="tile__label">contact</span>
      <span class="tile__value">t: (555) 416-9073</span>
    </div>
  </section>
  <span class="side-label side-label--back">back</span>

</div>
</body>
</html>
```